Sports hypnotherapist needs electronic letterhead design

Need a simple but classy design for a letterhead that looks good when printed. Its for a hypnotherapist who specialises in elite sport. Should have my company name and address and website details on it. I specialise in footballers.
Should look good electronically and when printed.
Include all contact details as shown in the must haves.

Target Market(s)

Sports people, elite sport.

Industry/Entity Type

Hypnotherapy

Font styles to use
Sans Serif

Colors

Designer to choose colors to be used in the design.

Requirements
Must have
• NEEDS TO BE DESIGNED IN MS WORD
• Logo +
• Blue Heron Hypnotherapists
• 27 Marlowe Close
• Bracknell
• RG41 5PL
• Tel: 07700 900461
• E: blueheroncoaching@mailvale.com
• www: http://www.blue-heron-clinic.co.uk.
• Derek Ashworth
• Clinical hypnotherapist, hypnoanalyst, mental resilience coach, MSc, Dip PHH
Nice to have
• A watermark?
• Plenty of space for the A4 letter
• Prints well.
Should not have
• Too much clutter.
• Too much colour that will be costly to print.

```html
<!DOCTYPE html>
<html lang="en">
<head>
<meta charset="utf-8">
<title>Blue Heron Hypnotherapists – Letterhead</title>
<link href="https://fonts.googleapis.com/css2?family=Open+Sans:wght@400;600;700&family=Roboto+Condensed:wght@400&display=swap" rel="stylesheet">
<style>
  :root{
    --ink:#1f2226;
    --text:#5a5d61;
    --blue:#4fb0e6;
    --sig-blue:#1f78c1;
    --band:#23272b;
    --rule:#6b6e72;
    --paper:#fafafa;
    --backdrop:#e9e9e9;
    --mark-grey:#e6e6e6;
    --mark-blue:#eaf4fb;
  }
  *{box-sizing:border-box;margin:0;padding:0}
  html,body{width:1102px;height:1200px;overflow:hidden;background:var(--backdrop)}
  body{font-family:"Open Sans",Arial,sans-serif}
  .letterhead{position:absolute;left:127px;top:0;width:848px;height:1200px;background:var(--paper);overflow:hidden}
  .watermark{position:absolute;left:255px;top:305px;width:435px;height:670px;border-radius:60px 60px 30px 30px;
    background:linear-gradient(110deg,var(--mark-grey) 0%,var(--mark-grey) 45%,var(--mark-blue) 70%,rgba(234,244,251,0) 100%);opacity:.75}
  .brand{position:absolute;left:58px;top:62px;display:flex;align-items:center;gap:12px}
  .brand-dot{width:34px;height:34px;border-radius:50%;background:var(--blue);flex:none}
  .brand-name{font-weight:700;font-size:29px;line-height:33px;color:var(--ink)}
  .header-rule{position:absolute;left:345px;right:58px;top:114px;height:1.5px;background:var(--rule)}
  .practitioner{position:absolute;right:58px;top:86px;text-align:right}
  .practitioner-name{font-weight:700;font-size:20px;color:var(--blue);line-height:26px}
  .practitioner-role{margin-top:9px;font-size:11.5px;line-height:15.5px;color:var(--ink)}
  .letter-body{position:absolute;left:84px;top:307px;width:680px;font-size:13px;line-height:21.7px;color:var(--text);text-align:justify}
  .salutation{margin-bottom:44px}
  .letter-body p+p{margin-top:21.5px}
  .sign-off{position:absolute;left:84px;top:832px;color:var(--text)}
  .sign-off-label{font-weight:700;font-size:13px;color:#4a4d51}
  .signature{display:block;margin-top:20px;width:205px;height:44px;border-radius:22px;background:linear-gradient(90deg,rgba(31,120,193,.18),rgba(31,120,193,.05))}
  .sign-off-title{margin-top:14px;font-size:13px}
  .contact-bar{position:absolute;left:84px;right:84px;top:1150px;display:flex;justify-content:space-between;align-items:center;
    font-family:"Roboto Condensed",Arial,sans-serif;font-size:13.5px;color:var(--ink)}
  .contact-item{display:flex;align-items:center;gap:5px;white-space:nowrap}
  .contact-item svg{width:12px;height:12px;fill:var(--blue);flex:none}
  .footer-band{position:absolute;left:0;right:0;bottom:0;height:12px;background:var(--band)}
  .footer-band-accent{position:absolute;left:547px;width:225px;top:0;bottom:0;background:var(--blue)}
</style>
</head>
<body>
<main class="letterhead">
  <div class="watermark" role="img" aria-label="Faint watermark of a suited coach silhouette with a sprinting athlete"></div>

  <header>
    <div class="brand">
      <span class="brand-dot"></span>
      <div class="brand-name">Blue Heron<br>Hypnotherapists</div>
    </div>
    <div class="header-rule"></div>
    <div class="practitioner">
      <div class="practitioner-name">Derek Ashworth</div>
      <div class="practitioner-role">Clinical Hypnotherapist,<br>Hypnoanalyst, Mental<br>Resilience Coach, Msc, Dip Phh</div>
    </div>
  </header>

  <section class="letter-body">
    <div class="salutation">Dear Sir,</div>
    <p>Lorem Ipsum is simply dummy text of the printing and typesetting industry. Lorem Ipsum has been the industry's standard dummy text ever since the 1500s, when an unknown printer took a galley of type and scrambled it to make a type specimen book. It has survived not only five centuries, but also the leap into electronic typesetting, remaining essentially unchanged. It was popularised in the 1960s with the release of Letraset sheets containing Lorem Ipsum passages, and more recently with desktop publishing software like Aldus PageMaker including versions of Lorem Ipsum.</p>
    <p>Lorem Ipsum is simply dummy text of the printing and typesetting industry. Lorem Ipsum has been the industry's standard dummy text ever since the 1500s, when an unknown printer took a galley of type and scrambled it to make a type specimen book. It has survived not only five centuries, but also the leap into electronic typesetting, remaining essentially unchanged. It was popularised in the 1960s with the release of Letraset sheets containing Lorem Ipsum passages, and more recently with desktop publishing software like Aldus PageMaker including versions of Lorem Ipsum.</p>
    <p>Lorem Ipsum is simply dummy text of the printing and typesetting industry. Lorem Ipsum has been the industry's standard dummy text ever since the 1500s, when an unknown printer took a galley of type and scrambled it to make a type specimen book.</p>
  </section>

  <section class="sign-off">
    <div class="sign-off-label">Your Name</div>
    <span class="signature" role="img" aria-label="Handwritten signature of Martin Selby"></span>
    <div class="sign-off-title">CEO &nbsp;|&nbsp; Owner</div>
  </section>

  <footer class="contact-bar">
    <span class="contact-item">
      <svg viewBox="0 0 24 24"><path d="M6.6 10.8a15.1 15.1 0 0 0 6.6 6.6l2.2-2.2c.3-.3.7-.4 1-.2 1.1.4 2.3.6 3.6.6.6 0 1 .4 1 1V20c0 .6-.4 1-1 1A17 17 0 0 1 3 4c0-.6.4-1 1-1h3.5c.6 0 1 .4 1 1 0 1.3.2 2.5.6 3.6.1.3 0 .7-.2 1z"/></svg>07700 900461</span>
    <span class="contact-item">
      <svg viewBox="0 0 24 24"><path d="M2 5h20v14H2zM3.5 6.5l8.5 6.5 8.5-6.5v-.1H3.5z"/></svg>blueheroncoaching@mailvale.com</span>
    <span class="contact-item">
      <svg viewBox="0 0 24 24"><path d="M12 2a10 10 0 1 0 0 20 10 10 0 0 0 0-20zm6.9 6h-2.9a15.7 15.7 0 0 0-1.4-3.6A8 8 0 0 1 18.9 8zM12 4c.8 1.2 1.5 2.5 1.9 4h-3.8c.4-1.5 1.1-2.8 1.9-4zM4.3 14a8 8 0 0 1 0-4h3.4a16 16 0 0 0 0 4zm.8 2h2.9c.3 1.3.8 2.5 1.4 3.6A8 8 0 0 1 5.1 16zM8 8H5.1a8 8 0 0 1 4.3-3.6C8.8 5.5 8.3 6.7 8 8zm4 12c-.8-1.2-1.5-2.5-1.9-4h3.8c-.4 1.5-1.1 2.8-1.9 4zm2.3-6H9.7a14.7 14.7 0 0 1 0-4h4.6a14.7 14.7 0 0 1 0 4zm.3 5.6c.6-1.1 1.1-2.3 1.4-3.6h2.9a8 8 0 0 1-4.3 3.6zm1.7-5.6a16 16 0 0 0 0-4h3.4a8 8 0 0 1 0 4z"/></svg>www.blue-heron-clinic.co.uk</span>
    <span class="contact-item">
      <svg viewBox="0 0 24 24"><path d="M12 2a7 7 0 0 0-7 7c0 5.2 7 13 7 13s7-7.8 7-13a7 7 0 0 0-7-7zm0 9.5a2.5 2.5 0 1 1 0-5 2.5 2.5 0 0 1 0 5z"/></svg>27 Marlowe Close Bracknell RG41 5PL</span>
  </footer>

  <div class="footer-band"><div class="footer-band-accent"></div></div>
</main>
</body>
</html>
```